Boring Fiberglass Repair Company needs creative business cards

The Fiberglass Repair industry isn't very fun or creative but we'd like a business card that communicates a fresh, modern, and service-oriented feel. We repair bathroom fixtures (bath tubs, showers, etc) which are made out of fiberglass. Our fiberglass repair service will be sold to bathtub manufacturers and also businesses that sell bathtubs. We will also offer our services to home owners that have broken showers and bathtubs.
Target Market(s)
Home builders, plumbing wholesalers, home owners
Contact Information for Business Card
Name
Phone Number
Email Address
Business Address
Tag line: "Quality Craftsmanship Today"

```html
<!DOCTYPE html>
<html lang="en">
<head>
<meta charset="utf-8">
<title>Mesa Ridge Fiberglass – Business Cards</title>
<link rel="stylesheet" href="https://fonts.googleapis.com/css2?family=Poppins:wght@400;500;600;800&display=swap">
<style>
  :root {
    --navy: #233f8a;
    --navy-deep: #1b2f6e;
    --red: #d8232f;
    --white: #ffffff;
    --paper: #f1f1f1;
    --backdrop: #e9e5de;
  }
  * { margin: 0; padding: 0; box-sizing: border-box; }
  html, body { width: 1200px; height: 780px; overflow: hidden; }
  body {
    background: var(--backdrop);
    font-family: "Poppins", sans-serif;
    position: relative;
  }
  .card {
    position: absolute;
    top: 241px;
    width: 520px;
    height: 298px;
    border-radius: 16px;
    overflow: hidden;
    box-shadow: 0 10px 28px rgba(0,0,0,0.22);
  }
  .card-front { left: 50px; background: var(--navy); }
  .card-back {
    left: 630px;
    background: radial-gradient(ellipse at 50% 45%, #2a4a9c 0%, var(--navy) 55%, var(--navy-deep) 100%);
  }
  .wave { position: absolute; inset: 0; width: 100%; height: 100%; }

  .brand {
    position: absolute;
    font-family: "Poppins", sans-serif;
    font-weight: 800;
    line-height: 1;
    text-transform: uppercase;
  }
  .brand-name { display: block; font-size: 34px; letter-spacing: 0.5px; }
  .brand-sub { display: block; font-size: 13px; letter-spacing: 11px; margin-top: 8px; }
  .card-front .brand { left: 30px; top: 78px; color: var(--navy); }
  .card-back .brand {
    left: 0; right: 0; top: 50%;
    transform: translateY(-50%);
    text-align: center;
    color: var(--white);
  }
  .card-back .brand-name { font-size: 38px; }
  .card-back .brand-sub { font-size: 14px; letter-spacing: 13px; margin-top: 10px; padding-left: 13px; }

  .tagline {
    position: absolute;
    right: 20px;
    top: 146px;
    font-size: 12px;
    font-weight: 400;
    color: var(--white);
    letter-spacing: 0.2px;
  }
  .contact {
    position: absolute;
    left: 226px;
    top: 178px;
    color: var(--white);
  }
  .contact-name {
    font-size: 19px;
    font-weight: 600;
    text-transform: uppercase;
    margin-bottom: 8px;
    letter-spacing: 0.3px;
    line-height: 1.2;
  }
  .contact-name .first { color: var(--red); }
  .contact-list { list-style: none; }
  .contact-list li {
    display: flex;
    align-items: center;
    gap: 8px;
    font-size: 12px;
    line-height: 1;
    margin-bottom: 7px;
  }
  .contact-icon {
    width: 15px; height: 15px;
    flex: none;
  }
</style>
</head>
<body>

  <section class="card card-front" aria-label="Business card front">
    <svg class="wave" viewBox="0 0 520 298" preserveAspectRatio="none" aria-hidden="true">
      <path fill="var(--white)" transform="translate(20 14)" d="M0,0 H420 C400,70 360,115 290,140 C200,172 110,200 70,298 H0 Z"/>
      <path fill="var(--red)" transform="translate(16 11)" d="M0,0 H420 C400,70 360,115 290,140 C200,172 110,200 70,298 H0 Z"/>
      <path fill="var(--paper)" d="M0,0 H420 C400,70 360,115 290,140 C200,172 110,200 70,298 H0 Z"/>
    </svg>

    <div class="brand">
      <span class="brand-name">Mesa Ridge</span>
      <span class="brand-sub">Fiberglass</span>
    </div>

    <p class="tagline">Quality Craftsmanship Today</p>

    <div class="contact">
      <p class="contact-name"><span class="first">Jordan</span> Reyes</p>
      <ul class="contact-list">
        <li>
          <svg class="contact-icon" viewBox="0 0 16 16" aria-hidden="true">
            <circle cx="8" cy="8" r="8" fill="var(--red)"/>
            <rect x="5.5" y="3.5" width="5" height="9" rx="1" fill="none" stroke="var(--white)" stroke-width="1.2"/>
            <circle cx="8" cy="11" r="0.6" fill="var(--white)"/>
          </svg>
          555-014-2280
        </li>
        <li>
          <svg class="contact-icon" viewBox="0 0 16 16" aria-hidden="true">
            <circle cx="8" cy="8" r="8" fill="var(--red)"/>
            <rect x="4" y="5" width="8" height="6" fill="none" stroke="var(--white)" stroke-width="1.1"/>
            <path d="M4,5 L8,8.5 L12,5" fill="none" stroke="var(--white)" stroke-width="1.1"/>
          </svg>
          hello@mesaridgefiber.com
        </li>
        <li>
          <svg class="contact-icon" viewBox="0 0 16 16" aria-hidden="true">
            <circle cx="8" cy="8" r="8" fill="var(--red)"/>
            <circle cx="8" cy="8" r="4.2" fill="none" stroke="var(--white)" stroke-width="1"/>
            <ellipse cx="8" cy="8" rx="1.8" ry="4.2" fill="none" stroke="var(--white)" stroke-width="0.9"/>
            <line x1="3.8" y1="8" x2="12.2" y2="8" stroke="var(--white)" stroke-width="0.9"/>
          </svg>
          www.mesaridgefiber.com
        </li>
      </ul>
    </div>
  </section>

  <section class="card card-back" aria-label="Business card back">
    <div class="brand">
      <span class="brand-name">Mesa Ridge</span>
      <span class="brand-sub">Fiberglass</span>
    </div>
  </section>

</body>
</html>
```